To design a professional looking flyer for a mailbox drop.

On the front we would like the Loft logo, our email address (theloftcanberra@mailpinto.com) and A special offer
Sign on for six months get your first six weeks Free (saving of $302)
Sign on for three months get your first three weeks free (saving of $151)

On the back "5 things you can do NOW to look after your Mental Health''
1. Remain connected to supportive people. Spend time with and reach out to people who are a positive influence on you. Having a network of good relationships and taking part in social activities improves confidence, wellbeing and keeps our mind busy.
2. Be aware of negative thoughts. Thoughts arent necessarily facts and it can be easy to let our mind get away on us. Be aware of your negative thoughts and try not to give them power. Come up with a strategy so that when you notice yourself thinking negatively you can implement the strategy that overrides the thought, practice it regularly and overtime you’ll be the master of your mind, rather than your mind being the master of you!
3. Develop a daily routine that prioritises something you enjoy. Make YOU your non negotiable. We all lead busy lives, but its important to do something for ourselves that we enjoy and can look forward to. Taking a bath, coffee with a friend, a walk, reading before bed, gardening. Its nice to look back on your day and see we have done something for ourselves.
4. Exercise, movement is key! Daily exercise is best however, its been proven that as little as 45 mins of exercise three times a week can lessen feelings of depressions, anxiety and stress. Find something you enjoy doing, a gym class where the session is planned for you, walk in do your exercise, walk out and get on with your day, walking, running, dancing, just be sure to get it done. The benefits are endless. Gradually build it into your routine, exercise with a friend, it helps keep you both accountable and its more fun too!
5. Eat well. Our brain and gut are connected, this is known as the Gut Brain axis. Our GI tract releases neurotransmitters and hormones like serotonin and dopamine which affect brain function and mood. If the microbes in your gut are unbalanced it can lead to less production of the ‘happy hormones.’ Probiotics are key to balanced gut health, think probiotic yoghurts, kimchi, miso soup, sauerkraut or probiotic supplements. Vitamin D rich foods wil help too, eggs yolks, tuna, salmon. Lighten up on the sugary and processed food as these can inhibit the growth of good bacteria.

Industry/Entity Type

we are a gym

Colors

Designer to choose colors to be used in the design.

Requirements
Must have
• logo/s

```html
<!DOCTYPE html>
<html lang="en">
<head>
<meta charset="utf-8">
<title>The Loft Canberra – Mailbox Flyer</title>
<link href="https://fonts.googleapis.com/css2?family=Barlow:wght@400;500;700;800;900&family=Bebas+Neue&display=swap" rel="stylesheet">
<style>
  :root {
    --red: #ec1c24;
    --ink: #0b0b0c;
    --charcoal: #1e1e20;
    --white: #ffffff;
    --paper: #f2f2f2;
    --stage: #9a9a9a;
    --body-text: #e6e6e6;
  }
  * { margin: 0; padding: 0; box-sizing: border-box; }
  html, body { width: 1200px; height: 825px; overflow: hidden; }
  body { background: var(--stage); font-family: "Barlow", sans-serif; position: relative; }

  .flyer { position: absolute; top: 86px; width: 505px; height: 653px; overflow: hidden; }
  .flyer--front { left: 68px; background: var(--paper); }
  .flyer--back { left: 628px; background: var(--white); }

  /* FRONT */
  .hero-photo { position: absolute; inset: 0 0 auto 0; height: 430px;
    background: radial-gradient(ellipse 45% 60% at 72% 45%, #6a4a3c 0%, #2b211d 45%, transparent 75%),
                linear-gradient(180deg, #121212 0%, #1a1a1a 60%, #0e0e0e 100%); }
  .light-fade { position: absolute; left: 0; right: 0; top: 400px; height: 240px;
    background: linear-gradient(135deg, #e4e4e4 0%, #f7f7f7 50%, #ececec 100%); }
  .edge { position: absolute; left: 0; top: 0; width: 505px; height: 653px; }

  .brand { position: absolute; left: 47px; top: 53px; width: 196px; display: flex; align-items: center; gap: 8px; }
  .brand-mark { width: 44px; height: 44px; background: var(--red); flex: none; }
  .brand-name { font-family: "Barlow", sans-serif; font-weight: 800; font-size: 39px; color: var(--white); letter-spacing: 1px; line-height: 1; white-space: nowrap; }
  .tagline { position: absolute; left: 47px; top: 109px; width: 196px; text-align: center; color: var(--white);
    font-weight: 700; font-size: 8.4px; letter-spacing: 1.6px; }
  .city { position: absolute; left: 47px; top: 126px; width: 196px; text-align: center; color: var(--white);
    font-weight: 800; font-size: 11px; letter-spacing: 5px; }

  .offer-title { position: absolute; left: 47px; top: 169px; width: 196px; }
  .offer-title__top { height: 59px; border: 1.5px solid var(--red); border-bottom: none; background: var(--ink);
    color: var(--white); font-family: "Bebas Neue", sans-serif; font-size: 52px; line-height: 62px; text-align: center; }
  .offer-title__main { height: 75px; background: var(--red); color: var(--white); font-family: "Bebas Neue", sans-serif;
    font-size: 82px; line-height: 84px; text-align: center; letter-spacing: 1px; }

  .deal { position: absolute; left: 70px; width: 365px; height: 71px; border-radius: 4px; background: var(--charcoal);
    box-shadow: 0 6px 10px rgba(0,0,0,.25); overflow: hidden; }
  .deal--six { top: 427px; }
  .deal--three { top: 517px; }
  .deal__terms { position: absolute; left: 0; top: 0; width: 224px; height: 71px; background: var(--red);
    clip-path: polygon(0 0, 210px 0, 224px 50%, 210px 100%, 0 100%);
    display: flex; align-items: center; justify-content: center; padding-right: 14px;
    color: var(--white); font-weight: 800; font-size: 15.5px; line-height: 17.5px; text-align: center; text-transform: uppercase; }
  .deal__chevron { position: absolute; left: 210px; top: 0; width: 30px; height: 71px; background: #121213;
    clip-path: polygon(0 0, 14px 0, 28px 50%, 14px 100%, 0 100%, 14px 50%); }
  .deal__saving { position: absolute; left: 230px; right: 0; top: 8px; text-align: center; color: var(--white); }
  .deal__label { font-weight: 800; font-size: 18.5px; line-height: 20px; }
  .deal__amount { font-weight: 900; font-size: 38px; line-height: 38px; }

  .contact-tab { position: absolute; left: 82px; top: 604px; width: 341px; height: 30px; background: var(--charcoal);
    clip-path: polygon(20px 0, 321px 0, 341px 100%, 0 100%);
    color: var(--white); font-weight: 700; font-size: 17px; line-height: 32px; text-align: center; }
  .contact-tab__accent { position: absolute; top: 610px; width: 22px; height: 24px; background: var(--red); }
  .contact-tab__accent--left { left: 80px; clip-path: polygon(100% 0, 60% 100%, 0 100%, 0 100%, 40% 100%); clip-path: polygon(14px 0, 20px 0, 8px 100%, 0 100%); }
  .contact-tab__accent--right { left: 404px; clip-path: polygon(0 0, 6px 0, 22px 100%, 14px 100%); }
  .footer-band { position: absolute; left: 0; right: 0; top: 634px; height: 19px; background: var(--charcoal); }

  /* BACK */
  .back-photo { position: absolute; left: 0; right: 0; top: 140px; height: 440px;
    background: radial-gradient(ellipse 70% 60% at 60% 50%, #3a3a3c 0%, #232325 60%, #1b1b1d 100%); }
  .back-header { position: absolute; left: 0; right: 0; top: 0; height: 160px; background: var(--red); }
  .guide-title { position: absolute; left: 55px; top: 40px; width: 395px; color: var(--white); font-family: "Bebas Neue", sans-serif; text-align: center; }
  .guide-title__lead { font-size: 30.5px; line-height: 32px; letter-spacing: 0.1px; }
  .guide-title__main { font-size: 56px; line-height: 54px; margin-top: 5px; }

  .tips { list-style: none; }
  .tip { position: absolute; left: 49px; width: 406px; display: flex; align-items: center; }
  .tip__num { position: absolute; left: 0; width: 45px; height: 45px; border-radius: 50%; background: var(--white);
    border: 2px solid var(--red); box-shadow: 0 0 0 2px var(--white), 0 3px 6px rgba(0,0,0,.5);
    font-family: "Bebas Neue", sans-serif; font-size: 28px; line-height: 44px; text-align: center; color: var(--ink); }
  .tip__text { position: absolute; left: 60px; width: 346px; color: var(--body-text); font-size: 7.4px; line-height: 10.7px; text-align: justify; transform: translateY(-50%); }
  .tip--1 { top: 210px; } .tip--2 { top: 271px; } .tip--3 { top: 337px; } .tip--4 { top: 406px; } .tip--5 { top: 487px; }
  .tip__num { top: -22px; }

  .back-email { position: absolute; left: 0; right: 0; top: 594px; text-align: center; color: var(--red);
    font-weight: 700; font-size: 16.5px; letter-spacing: 4.6px; }
</style>
</head>
<body>

<section class="flyer flyer--front" aria-label="Front of flyer">
  <div class="hero-photo" role="img" aria-label="Gym photo: athlete carrying a red battle rope over his shoulder"></div>
  <div class="light-fade"></div>
  <svg class="edge" viewBox="0 0 505 653" aria-hidden="true">
    <path fill="#1a1a1a" d="M0 430 L0 400 L12 396 L20 376 L30 392 L44 370 L52 388 L66 362 L74 386 L88 366 L96 384 L110 358 L118 380 L134 364 L142 382 L156 356 L166 378 L180 362 L190 384 L204 360 L214 380 L228 350 L238 376 L252 362 L262 388 L276 368 L288 392 L300 372 L312 396 L326 370 L338 390 L352 364 L364 386 L378 358 L392 380 L404 362 L418 384 L432 364 L444 380 L458 356 L470 374 L484 358 L496 370 L505 362 L505 430 Z" opacity="0"/>
    <path fill="#e9e9e9" d="M0 653 L0 484 L12 470 L20 476 L30 458 L44 462 L52 448 L66 452 L74 440 L88 446 L96 432 L110 440 L118 428 L134 436 L142 422 L156 430 L166 416 L180 426 L190 410 L204 420 L214 404 L228 416 L238 398 L252 410 L262 394 L276 404 L288 388 L300 400 L312 384 L326 396 L338 380 L352 392 L364 378 L378 390 L392 374 L404 386 L418 372 L432 382 L444 366 L458 376 L470 362 L484 372 L496 360 L505 364 L505 653 Z" transform="translate(0 0) scale(1 1)"/>
    <path fill="#eeeeee" d="M0 653 L0 400 L10 412 L22 388 L34 404 L46 380 L58 398 L70 374 L84 394 L98 370 L110 392 L124 366 L138 388 L150 372 L164 394 L178 368 L192 392 L206 374 L220 398 L234 376 L248 400 L262 382 L276 404 L290 384 L304 402 L318 380 L332 398 L346 376 L360 394 L374 372 L388 390 L402 370 L416 386 L430 368 L444 384 L458 364 L472 378 L486 362 L505 372 L505 653 Z"/>
  </svg>

  <div class="brand">
    <span class="brand-mark"></span>
    <span class="brand-name">THE LOFT</span>
  </div>
  <p class="tagline">STABILITY · MOBILITY · CONDITIONING</p>
  <p class="city">CANBERRA</p>

  <h1 class="offer-title">
    <span class="offer-title__top" style="display:block">A SPECIAL</span>
    <span class="offer-title__main" style="display:block">OFFER</span>
  </h1>

  <div class="deal deal--six">
    <p class="deal__terms">Sign on for 6 months<br>get your<br>first six weeks free</p>
    <span class="deal__chevron"></span>
    <div class="deal__saving"><p class="deal__label">SAVING OF</p><p class="deal__amount">$302</p></div>
  </div>

  <div class="deal deal--three">
    <p class="deal__terms">Sign on for 3 months<br>get your first<br>three weeks free</p>
    <span class="deal__chevron"></span>
    <div class="deal__saving"><p class="deal__label">SAVING OF</p><p class="deal__amount">$151</p></div>
  </div>

  <span class="contact-tab__accent contact-tab__accent--left"></span>
  <span class="contact-tab__accent contact-tab__accent--right"></span>
  <p class="contact-tab">theloftcanberra@mailpinto.com</p>
  <div class="footer-band"></div>
</section>

<section class="flyer flyer--back" aria-label="Back of flyer">
  <div class="back-photo" role="img" aria-label="Dimmed photo of a group gym class training"></div>
  <div class="back-header"></div>
  <svg class="edge" viewBox="0 0 505 653" aria-hidden="true">
    <path fill="#ec1c24" d="M0 150 L0 160 L10 172 L20 158 L30 176 L42 156 L52 172 L64 150 L76 168 L88 148 L100 166 L112 146 L124 164 L138 142 L150 162 L162 140 L176 160 L188 138 L200 158 L214 136 L226 156 L240 138 L252 160 L266 140 L278 162 L292 142 L304 164 L318 144 L330 166 L344 146 L356 168 L370 148 L382 170 L396 150 L408 172 L422 152 L434 174 L448 154 L460 176 L474 156 L486 174 L505 156 L505 150 Z"/>
    <path fill="#ffffff" d="M0 653 L0 582 L12 566 L22 580 L34 558 L46 576 L58 554 L70 572 L84 550 L96 570 L110 548 L122 568 L136 546 L148 566 L162 544 L176 564 L188 542 L202 562 L216 544 L228 564 L242 546 L256 566 L270 548 L282 568 L296 550 L310 570 L322 552 L336 572 L350 554 L362 572 L376 552 L390 570 L402 550 L416 568 L430 548 L442 566 L456 546 L470 564 L484 548 L496 562 L505 552 L505 653 Z"/>
  </svg>

  <h2 class="guide-title">
    <span class="guide-title__lead" style="display:block">5 THINGS YOU CAN DO NOW TO LOOK AFTER</span>
    <span class="guide-title__main" style="display:block">YOUR MENTAL HEALTH</span>
  </h2>

  <ol class="tips">
    <li class="tip tip--1"><span class="tip__num">01</span><p class="tip__text">Remain connected to supportive people. Spend time with and reach out to people who are a positive influence on you. Having a network of good relationships and taking part in social activities improves confidence, wellbeing and keeps our mind busy.</p></li>
    <li class="tip tip--2"><span class="tip__num">02</span><p class="tip__text">Be aware of negative thoughts. Thoughts arent necessarily facts and it can be easy to let our mind get away on us. Be aware of your negative thoughts and try not to give them power. Come up with a strategy so that when you notice yourself thinking negatively you can implement the strategy that overrides the thought, practice it regularly and overtime you’ll be the master of your mind, rather than your mind being the master of you!</p></li>
    <li class="tip tip--3"><span class="tip__num">03</span><p class="tip__text">Develop a daily routine that prioritises something you enjoy. Make YOU your non negotiable. We all lead busy lives, but its important to do something for ourselves that we enjoy and can look forward to. Taking a bath, coffee with a friend, a walk, reading before bed, gardening. Its nice to look back on your day and see we have done something for ourselves.</p></li>
    <li class="tip tip--4"><span class="tip__num">04</span><p class="tip__text">Exercise, movement is key! Daily exercise is best however, its been proven that as little as 45 mins of exercise three times a week can lessen feelings of depressions, anxiety and stress. Find something you enjoy doing, a gym class where the session is planned for you, walk in do your exercise, walk out and get on with your day, walking, running, dancing, just be sure to get it done. The benefits are endless. Gradually build it into your routine, exercise with a friend, it helps keep you both accountable and its more fun too!</p></li>
    <li class="tip tip--5"><span class="tip__num">05</span><p class="tip__text">Eat well. Our brain and gut are connected, this is known as the Gut Brain axis. Our GI tract releases neurotransmitters and hormones like serotonin and dopamine which affect brain function and mood. If the microbes in your gut are unbalanced it can lead to less production of the ‘happy hormones.’ Probiotics are key to balanced gut health, think probiotic yoghurts, kimchi, miso soup, sauerkraut or probiotic supplements. Vitamin D rich foods wil help too, eggs yolks, tuna, salmon. Lighten up on the sugary and processed food as these can inhibit the growth of good bacteria.</p></li>
  </ol>

  <p class="back-email">theloftcanberra@mailpinto.com</p>
</section>

</body>
</html>
```